Business card for auto dealership

Looking for a clean modern design.
Would like attached logo incorporated

Industry/Entity Type

Car dealership

Contact Information for Business Card

Name, website, phone, cell, fax, email

```html
<!DOCTYPE html>
<html lang="en">
<head>
<meta charset="UTF-8">
<title>Halverson Truck &amp; Auto Sales – Business Card</title>
<link href="https://fonts.googleapis.com/css2?family=Lato:wght@400;700&display=swap" rel="stylesheet">
<style>
  :root {
    --backdrop: #ece8e1;
    --card: #ffffff;
    --ink: #000000;
    --text: #2b2b2b;
    --band-text: #ffffff;
  }
  * { margin: 0; padding: 0; box-sizing: border-box; }
  html, body { width: 1200px; height: 1200px; overflow: hidden; }
  body {
    background: var(--backdrop);
    font-family: "Lato", sans-serif;
    position: relative;
  }
  .card {
    position: absolute;
    left: 222px;
    width: 756px;
    height: 432px;
    background: var(--card);
    border-radius: 29px;
    overflow: hidden;
  }
  .card--front { top: 157px; }
  .card--back { top: 613px; }

  .brand-name {
    position: absolute;
    color: var(--ink);
    font-weight: 700;
    text-align: center;
    line-height: 1.05;
  }
  .card--front .brand-name {
    left: 34px; width: 392px; top: 160px;
    font-size: 48px;
  }
  .card--front .brand-name .brand-line2 { font-size: 24px; }
  .card--back .brand-name {
    left: 60px; width: 636px; top: 140px;
    font-size: 80px;
  }
  .card--back .brand-name .brand-line2 { font-size: 38px; }
  .brand-line2 { display: block; margin-top: 6px; }

  .divider {
    position: absolute;
    left: 459px; top: 117px;
    width: 2px; height: 199px;
    background: var(--ink);
  }
  .contact-block {
    position: absolute;
    left: 487px; top: 110px;
    color: var(--text);
  }
  .person-name {
    font-size: 29px; font-weight: 700; color: var(--ink);
    line-height: 36px;
  }
  .person-title {
    font-size: 18px; margin-top: 4px; line-height: 22px;
  }
  .contact-list { list-style: none; margin-top: 38px; }
  .contact-list li {
    display: flex; align-items: center;
    font-size: 19px; height: 29px;
  }
  .contact-list svg {
    width: 16px; height: 16px; margin-right: 9px; fill: var(--ink);
  }
  .web-band {
    position: absolute;
    left: 0; top: 374px; width: 100%; height: 27px;
    background: var(--ink);
    color: var(--band-text);
    font-size: 16px;
    text-align: center;
    line-height: 27px;
  }
</style>
</head>
<body>
  <section class="card card--front">
    <div class="brand-name">Halverson<span class="brand-line2">Truck &amp; Auto Sales</span></div>
    <div class="divider"></div>
    <div class="contact-block">
      <div class="person-name">Dana Whitfield</div>
      <div class="person-title">Managing Director</div>
      <ul class="contact-list">
        <li><svg viewBox="0 0 16 16" aria-hidden="true"><path d="M1 5c0-2 3-3 7-3s7 1 7 3v1h-4V5H5v1H1z"/><path d="M3 7h10l1 7H2z"/></svg>555-010-4011</li>
        <li><svg viewBox="0 0 16 16" aria-hidden="true"><path d="M4 0h8a1 1 0 0 1 1 1v14a1 1 0 0 1-1 1H4a1 1 0 0 1-1-1V1a1 1 0 0 1 1-1zm1 2v10h6V2zm3 11a1 1 0 1 0 0 2 1 1 0 0 0 0-2z"/></svg>555-010-2140</li>
        <li><svg viewBox="0 0 16 16" aria-hidden="true"><path d="M4 1h8v4H4z"/><path d="M1 6h14v6h-3v-2H4v2H1z"/><path d="M4 11h8v4H4z"/></svg>555-010-1774</li>
        <li><svg viewBox="0 0 16 16" aria-hidden="true"><path d="M1 4h14v1l-7 4-7-4z"/><path d="M1 6.5l7 4 7-4V13H1z"/></svg>dana@halversonauto.com</li>
      </ul>
    </div>
    <div class="web-band">www.Halversonauto.com</div>
  </section>

  <section class="card card--back">
    <div class="brand-name">Halverson<span class="brand-line2">Truck &amp; Auto Sales</span></div>
  </section>
</body>
</html>
```